Anchored Willow Website

Would like a website designed for my fitness and nutrition coaching company Anchor Willow. I have a company logo and would like to keep the page layout clean and simple. Needs to look great on computer and mobile devices.

Target Market(s)

Target market is individuals looking to make changes in their health and nutrition with the help of an online coach.

Industry/Entity Type

Fitness

Number of Pages Required

2 page

Colors
3176b5
0355a3
85acd3
cedeed
f8fcfd
ffffff

Requirements
Must have
• The first page should have the company logo and name towards the top and below that client before and after photos scrolling or displaying in some manner. Also would like a section that states services offered and a section about myself since I am the primary coach for clients.

```html
<!DOCTYPE html>
<html lang="en">
<head>
<meta charset="utf-8">
<title>Anchored Willow – Fitness &amp; Nutrition Coaching</title>
<link href="https://fonts.googleapis.com/css2?family=Roboto:wght@400;500;700;900&display=swap" rel="stylesheet">
<style>
:root{
  --blue:#3176b5;
  --blue-deep:#0355a3;
  --blue-soft:#85acd3;
  --blue-pale:#cedeed;
  --ice:#f8fcfd;
  --white:#ffffff;
  --ink:#2b2b2b;
  --text:#6d6d6d;
  --dark:#1f1f21;
  --dark-2:#2a2a2d;
  --line:#e3e3e3;
}
*{box-sizing:border-box;margin:0;padding:0}
html,body{width:1200px;height:3540px;overflow:hidden}
body{font-family:"Roboto",Arial,sans-serif;color:var(--text);background:var(--white);font-size:13px;line-height:1.6}
.page{position:relative;width:1200px;height:3540px}
section,header,footer,nav{position:relative;width:1200px}
.section-title{text-align:center;font-weight:900;font-size:30px;color:var(--ink);letter-spacing:.5px;text-transform:uppercase}
.section-title::after{content:"";display:block;width:60px;height:3px;background:var(--blue);margin:12px auto 0}
.photo{display:block}

/* header */
.topbar{height:112px;display:flex;align-items:center;justify-content:space-between;padding:0 50px;background:var(--white)}
.brand{display:flex;align-items:center;gap:12px}
.brand-mark{width:44px;height:44px;border-radius:50%;background:var(--blue)}
.brand-name{font-weight:900;font-size:22px;color:var(--blue);letter-spacing:1px;text-transform:uppercase}
.contacts{display:flex;gap:46px}
.contact{display:flex;align-items:center;gap:10px;font-size:12px;line-height:1.4;color:var(--text)}
.contact svg{width:30px;height:30px}
.contact strong{display:block;color:var(--ink);font-weight:500}
.mainnav{height:32px;background:var(--dark);display:flex;align-items:center;justify-content:space-between;padding:0 50px 0 40px}
.mainnav ul{display:flex;list-style:none;height:100%}
.mainnav li{color:#ddd;font-size:11px;font-weight:500;padding:0 16px;display:flex;align-items:center;text-transform:uppercase}
.mainnav li.active{background:var(--blue);color:var(--white)}
.social{display:flex;gap:6px}
.social span{width:18px;height:18px;border:1px solid #666;display:block}

/* hero */
.hero{height:416px;display:flex}
.hero .photo{width:600px;height:416px}
.hero .before{background:linear-gradient(135deg,#c9c3bd,#8d8278 60%,#b8aea4)}
.hero .after{background:linear-gradient(135deg,#d6d2cd,#9a8b7d 60%,#cfc8c1)}
.hero-label{position:absolute;top:20px;font-size:46px;font-weight:900;color:var(--white);letter-spacing:2px}
.hero-label.left{left:26px}.hero-label.right{right:26px}

/* welcome */
.welcome{height:240px;background:var(--blue);padding-top:40px;text-align:center}
.welcome .section-title{color:var(--white)}
.welcome .section-title::after{background:var(--white)}
.welcome p{width:900px;margin:20px auto 0;color:var(--blue-pale);font-size:12px;line-height:1.6}
.services{height:260px;background:var(--ice)}
.service-list{position:absolute;top:-30px;left:160px;display:flex;gap:20px}
.service{width:280px;height:280px;background:var(--white);border:2px solid var(--blue);text-align:center}
.service .photo{height:170px}
.service h3{color:var(--blue);font-size:18px;font-weight:900;margin-top:14px;text-transform:uppercase;line-height:1.3}
.service p{font-size:11px;padding:6px 24px 0;line-height:1.5}

/* about */
.about{height:560px;padding-top:50px}
.about-body{position:absolute;top:140px;left:160px;width:880px;height:360px}
.about-frame{position:absolute;left:0;top:0;width:260px;height:320px;background:#3a3a3a}
.about-photo{position:absolute;left:24px;top:24px;width:260px;height:320px;background:linear-gradient(160deg,#d8dde2,#8fa1ad 55%,#5f7480)}
.about-text{position:absolute;left:320px;top:10px;width:560px}
.about-text h3{font-size:20px;color:var(--ink);font-weight:700;margin-bottom:12px}
.about-text h3::after{content:"";display:block;width:40px;height:2px;background:var(--blue);margin-top:8px}
.about-text p{font-size:12px;margin-bottom:10px}
.btn{display:inline-block;background:var(--blue);color:var(--white);font-size:11px;font-weight:700;padding:9px 20px;text-transform:uppercase;margin-top:6px}

/* gallery */
.gallery{height:600px;background:var(--dark-2);padding-top:46px}
.gallery .section-title{color:var(--white)}
.filters{display:flex;justify-content:center;gap:12px;margin-top:24px}
.filters span{border:1px solid #555;color:#ddd;font-size:11px;font-weight:700;padding:6px 22px;text-transform:uppercase}
.filters span.active{background:var(--blue);border-color:var(--blue);color:var(--white)}
.grid{position:absolute;left:160px;top:190px;width:880px;display:grid;grid-template-columns:repeat(4,205px);gap:20px 20px}
.grid .photo{height:150px}
.g1{background:linear-gradient(135deg,#4b6c8e,#a37a64)}
.g2{background:linear-gradient(135deg,#8fc06a,#e6a95a)}
.g3{background:linear-gradient(135deg,#5b5b62,#9c8f84)}
.g4{background:linear-gradient(135deg,#3d4a57,#8b949c)}
.g5{background:linear-gradient(135deg,#9ac46a,#d9733f)}
.g6{background:linear-gradient(135deg,#6b7d92,#c1a287)}
.g7{background:linear-gradient(135deg,#6e6e6e,#b5a89a)}
.g8{background:linear-gradient(135deg,#c7a98d,#8c6d58)}

/* blog */
.blog{height:560px;padding-top:46px}
.posts{position:absolute;left:160px;top:140px;display:flex;gap:40px}
.post{width:420px;height:360px;display:flex;border:1px solid var(--line)}
.post .photo{width:200px;height:358px}
.p1{background:linear-gradient(170deg,#e8e6e4,#b69a84 60%,#e1dcd7)}
.p2{background:linear-gradient(170deg,#f0c38a,#8a6a4f 60%,#d9c2a3)}
.post-body{position:relative;width:218px;padding:90px 16px 0}
.date{position:absolute;top:0;left:0;width:64px;height:64px;background:var(--blue);color:var(--white);text-align:center;font-weight:900;font-size:22px;line-height:1;padding-top:12px}
.date small{display:block;font-size:11px;font-weight:500;margin-top:4px}
.post h4{font-size:13px;color:var(--ink);font-weight:700;line-height:1.4;margin-bottom:10px}
.post p{font-size:11px}
.meta{position:absolute;bottom:16px;left:16px;right:16px;display:flex;justify-content:space-between;font-size:10px;border-top:1px solid var(--line);padding-top:8px}

/* testimonials */
.testimonials{height:340px;background:var(--ice);padding-top:40px}
.quote-box{position:absolute;left:160px;top:120px;width:880px;height:130px;background:var(--blue);color:var(--white);text-align:center;padding:26px 60px 0;font-size:12px}
.quote-box cite{display:block;font-style:normal;margin-top:16px;font-size:11px;color:var(--blue-pale)}
.avatar{position:absolute;left:575px;top:266px;width:50px;height:50px;border-radius:50%;background:var(--blue-soft);border:3px solid var(--white)}

/* footer */
.site-footer{height:392px;background:var(--dark);padding:50px 160px 0;color:#9a9a9a}
.cols{display:flex;gap:60px}
.col{width:253px}
.col h5{color:var(--white);font-size:14px;font-weight:700;margin-bottom:14px}
.col p{font-size:11px;margin-bottom:10px}
.field{height:24px;border:1px solid #444;margin-bottom:8px;font-size:10px;padding:4px 8px;color:#777;line-height:1.4}
.field.tall{height:44px}
.send{display:inline-block;background:var(--blue);color:var(--white);font-size:10px;padding:4px 14px}
.tweet{display:flex;gap:10px;margin-bottom:14px;font-size:11px}
.tweet i{flex:none;width:14px;height:14px;background:#555;border-radius:2px;margin-top:3px}
.infobar{position:absolute;left:160px;top:300px;width:880px;height:40px;background:var(--blue);display:flex;align-items:center;justify-content:space-between;padding:0 22px;color:var(--white);font-size:12px}
.copyright{position:absolute;left:160px;top:352px;width:880px;display:flex;justify-content:space-between;font-size:10px;color:#777}
</style>
</head>
<body>
<div class="page">

<header class="topbar">
  <div class="brand"><span class="brand-mark"></span><span class="brand-name">Anchored Willow</span></div>
  <div class="contacts">
    <div class="contact">
      <svg viewBox="0 0 30 30"><circle cx="15" cy="15" r="12" fill="none" stroke="#3176b5" stroke-width="2"/><path d="M15 8v7l5 3" fill="none" stroke="#3176b5" stroke-width="2"/></svg>
      <div><strong>Monday - Friday 08:00-19:00</strong>Saturday and Sunday closed</div>
    </div>
    <div class="contact">
      <svg viewBox="0 0 30 30"><path d="M9 5l4 5-2 3c1 3 3 5 6 6l3-2 5 4-2 4C13 25 5 17 5 7z" fill="#3176b5"/></svg>
      <div><strong>(555) 214-3921</strong>Call us now</div>
    </div>
    <div class="contact">
      <svg viewBox="0 0 30 30"><path d="M15 3a8 8 0 0 1 8 8c0 6-8 16-8 16S7 17 7 11a8 8 0 0 1 8-8z" fill="#3176b5"/><circle cx="15" cy="11" r="3" fill="#fff"/></svg>
      <div><strong>Address</strong>hello@anchoredwillow.com</div>
    </div>
  </div>
</header>

<nav class="mainnav">
  <ul>
    <li class="active">Home</li><li>About us</li><li>Fitness and nutrition</li><li>Coaching</li><li>Blog</li><li>Contact us</li>
  </ul>
  <div class="social"><span></span><span></span><span></span><span></span></div>
</nav>

<section class="hero">
  <div class="photo before" role="img" aria-label="Client before photo, tank top, studio background"></div>
  <div class="photo after" role="img" aria-label="Client after photo, fit physique, studio background"></div>
  <span class="hero-label left">BEFORE</span>
  <span class="hero-label right">AFTER</span>
</section>

<section class="welcome">
  <h2 class="section-title">Welcome to Anchored Willow</h2>
  <p>Real change starts with a plan that fits your life. We pair structured training with simple, sustainable nutrition so every client builds strength, energy and confidence. Our online coaching keeps you accountable week after week, with clear goals, honest feedback and steady progress you can see and feel. Whether you are starting out or coming back, we meet you where you are and guide each step forward.</p>
</section>

<section class="services">
  <div class="service-list">
    <article class="service">
      <div class="photo" style="background:linear-gradient(135deg,#c8dcea,#5d8fb8)" role="img" aria-label="Woman training with light dumbbells"></div>
      <h3>Fitness</h3>
      <p>Custom training plans built around your goals, schedule and equipment, updated as you grow stronger.</p>
    </article>
    <article class="service">
      <div class="photo" style="background:linear-gradient(135deg,#e9efe0,#9cc06e)" role="img" aria-label="Woman with fresh fruit and vegetables"></div>
      <h3>Nutrition</h3>
      <p>Simple eating guidance and meal ideas that fuel your training without strict diets or guesswork.</p>
    </article>
    <article class="service">
      <div class="photo" style="background:linear-gradient(135deg,#b9b2aa,#5f5650)" role="img" aria-label="Coach guiding a client at the gym"></div>
      <h3>Coaching</h3>
      <p>Weekly check-ins, progress reviews and direct support to keep you consistent and motivated.</p>
    </article>
  </div>
</section>

<section class="about">
  <h2 class="section-title">About Myself</h2>
  <div class="about-body">
    <div class="about-frame"></div>
    <div class="about-photo" role="img" aria-label="Portrait of the head coach in a gym"></div>
    <div class="about-text">
      <h3>Jenna Calloway</h3>
      <p>I am a certified fitness and nutrition coach who has spent years helping people rebuild their habits and their health. My own journey taught me that lasting results come from small, steady changes rather than quick fixes.</p>
      <p>I work with every client personally, shaping training and nutrition plans around real schedules, real families and real goals. Together we set clear targets, track progress and adjust along the way so you always know what comes next.</p>
      <p>Online coaching lets me support you wherever you are. You get structure, accountability and honest encouragement, all designed to help you feel stronger and more confident in your body.</p>
      <span class="btn">Read more</span>
    </div>
  </div>
</section>

<section class="gallery">
  <h2 class="section-title">Our Gallery</h2>
  <div class="filters"><span class="active">All</span><span>Fitness</span><span>Nutrition</span><span>Coaching</span></div>
  <div class="grid">
    <div class="photo g1" role="img" aria-label="Group workout"></div>
    <div class="photo g2" role="img" aria-label="Healthy meal ingredients"></div>
    <div class="photo g3" role="img" aria-label="Coach spotting a lift"></div>
    <div class="photo g4" role="img" aria-label="Strength training"></div>
    <div class="photo g5" role="img" aria-label="Fresh fruit bowl"></div>
    <div class="photo g6" role="img" aria-label="Stretching session"></div>
    <div class="photo g7" role="img" aria-label="Gym equipment"></div>
    <div class="photo g8" role="img" aria-label="Smiling client after training"></div>
  </div>
</section>

<section class="blog">
  <h2 class="section-title">Latest Blog</h2>
  <div class="posts">
    <article class="post">
      <div class="photo p1" role="img" aria-label="Athlete with boxing gloves"></div>
      <div class="post-body">
        <div class="date">16<small>DEC</small></div>
        <h4>Five simple habits that keep your training on track</h4>
        <p>Consistency beats intensity. These small daily habits make it easier to show up, recover well and keep moving forward.</p>
        <div class="meta"><span>Comments</span><span>Read more</span></div>
      </div>
    </article>
    <article class="post">
      <div class="photo p2" role="img" aria-label="Smiling people at a gym"></div>
      <div class="post-body">
        <div class="date">16<small>DEC</small></div>
        <h4>Eating well on busy weeks without stress</h4>
        <p>Quick planning tips and easy meals that help you stay fuelled when work and family keep you on the go.</p>
        <div class="meta"><span>Comments</span><span>Read more</span></div>
      </div>
    </article>
  </div>
</section>

<section class="testimonials">
  <h2 class="section-title">Testimonials</h2>
  <blockquote class="quote-box">
    “Working with my coach changed how I train and how I eat. The plans were clear, the check-ins kept me honest, and for the first time I stuck with it long enough to see real results.”
    <cite>Client name</cite>
  </blockquote>
  <div class="avatar" role="img" aria-label="Client portrait"></div>
</section>

<footer class="site-footer">
  <div class="cols">
    <div class="col">
      <h5>Shortly About us</h5>
      <p>Online fitness and nutrition coaching for people ready to build healthier habits that last.</p>
      <p>Personal plans, weekly support and steady progress from wherever you are.</p>
    </div>
    <div class="col">
      <h5>Request Quote</h5>
      <div class="field">Name</div>
      <div class="field">Email</div>
      <div class="field tall">Message</div>
      <span class="send">Submit</span>
    </div>
    <div class="col">
      <h5>Latest Tweets</h5>
      <div class="tweet"><i></i><span>New client spots open for January coaching. Reserve yours today.</span></div>
      <div class="tweet"><i></i><span>Quick tip: plan tomorrow's meals tonight and stay on track.</span></div>
    </div>
  </div>
  <div class="infobar">
    <span>hello@anchoredwillow.com</span>
    <span>Call Now : (555) 214-3921</span>
    <span>Fax : (555) 214-3922</span>
  </div>
  <div class="copyright"><span>Home &nbsp; About &nbsp; Services &nbsp; Blog &nbsp; Contact</span><span>© Anchored Willow. All rights reserved.</span></div>
</footer>

</div>
</body>
</html>
```